One of Australia's fastest growing Financial Company looking for an updated business card design!

Meridale Holdings Australia is looking for an updated design for our business cards. We would like to keep up our professional appearances and have get new exciting design that fits our company.

The Meridale aim is to facilitate and assist clients in every financial requirement that may arise in financial areas.

We would to see the design to use colour blue and we like the clouds in the background. We have attached two designs we have use before but we need something with more professional and easy to read design.

We would like the website in the back of the card; the employees name more central and stands out; only a postal address; a list of all our locations along the bottom (Sydney, Melbourne, Brisbane, Singapore)

Looking forward to seeing the designs come in!

Target Market(s)

Other Industry Professionals
Middle Class Families

Industry/Entity Type

Finance

Contact Information for Business Card

Name; Company Role; Office Number; Mobile Number; Email Address; Website; Postal Address; Locations

Font styles to use
Serif
Sans Serif

Colors
0492cd
33a6d7
85cae6
85acd3
3176b5
0455a3
cee9f5
d5e2ee

Requirements
Must have
• Name; Company Role; Office Number; Mobile Number; Email Address; Website; Postal Address; Locations
Nice to have
• The colour blue, clouds on the background

```html
<!DOCTYPE html>
<html lang="en">
<head>
<meta charset="utf-8">
<title>Meridale Holdings Australia – Business Card</title>
<link rel="stylesheet" href="https://fonts.googleapis.com/css2?family=Montserrat:wght@400;500;600;700&display=swap">
<style>
  :root {
    --backdrop: #2a2a2c;
    --card-white: #ffffff;
    --brand-blue: #0f74bd;
    --brand-blue-deep: #0455a3;
    --text-blue: #1a6fb5;
    --accent-red: #e8333a;
    --pale-blue: #cee9f5;
  }
  * { box-sizing: border-box; margin: 0; padding: 0; }
  html, body {
    width: 1200px; height: 900px; overflow: hidden;
    background: var(--backdrop);
    font-family: "Montserrat", Arial, sans-serif;
  }
  .canvas { position: relative; width: 1200px; height: 900px; }

  .card {
    position: absolute;
    width: 560px; height: 320px;
    border-radius: 22px;
    overflow: hidden;
    background: var(--card-white);
    box-shadow: 0 14px 30px rgba(0,0,0,.45);
  }

  /* Front */
  .card-front { left: 90px; top: 110px; }
  .front-brand {
    position: absolute; left: 70px; top: 118px;
    display: flex; align-items: center; gap: 20px;
  }
  .brand-dot {
    width: 54px; height: 54px; border-radius: 50%;
    background: var(--brand-blue);
  }
  .brand-name {
    font-size: 78px; font-weight: 600; line-height: 1;
    color: var(--brand-blue); letter-spacing: -1px;
  }
  .front-web {
    position: absolute; right: 34px; bottom: 30px;
    font-size: 15px; font-weight: 500; color: var(--text-blue);
  }
  .front-web b { color: var(--accent-red); font-weight: 700; }

  /* Back */
  .card-back { left: 550px; top: 470px; }
  .back-field { position: absolute; inset: 0; }
  .holder {
    position: absolute; left: 34px; top: 140px; color: #fff;
  }
  .holder-name { font-size: 22px; font-weight: 700; letter-spacing: 1.5px; }
  .holder-role { font-size: 14px; font-weight: 400; letter-spacing: 1px; margin-top: 2px; }

  .contact {
    position: absolute; right: 26px; top: 62px;
    list-style: none; text-align: right;
    color: var(--text-blue); font-size: 16px; line-height: 1.3;
  }
  .contact li { display: flex; justify-content: flex-end; align-items: center; gap: 7px; }
  .contact svg { width: 13px; height: 13px; flex: none; }
  .contact .no-icon { padding-right: 20px; }

  .locations {
    position: absolute; right: 26px; bottom: 44px;
    text-align: right; color: var(--accent-red);
    font-size: 17px; font-weight: 700; letter-spacing: .5px; line-height: 1.25;
  }
</style>
</head>
<body>
<main class="canvas">

  <section class="card card-front" aria-label="Card front">
    <div class="front-brand">
      <span class="brand-dot"></span>
      <span class="brand-name">Meridale</span>
    </div>
    <p class="front-web">www.<b>meridale</b>.com</p>
  </section>

  <section class="card card-back" aria-label="Card back">
    <svg class="back-field" viewBox="0 0 560 320" preserveAspectRatio="none" aria-hidden="true">
      <rect width="560" height="320" fill="var(--card-white)"/>
      <path d="M0 0 H420 C330 70 290 170 300 320 H0 Z" fill="var(--brand-blue)"/>
    </svg>

    <div class="holder">
      <p class="holder-name">MARCUS ELLERY</p>
      <p class="holder-role">DIRECTOR</p>
    </div>

    <ul class="contact">
      <li class="no-icon">PO Box 2837</li>
      <li>02-5550-1427
        <svg viewBox="0 0 16 16"><path d="M2 6c0-2 3-3 6-3s6 1 6 3v1h-3V5.5H5V7H2z M4 8h8l1 5H3z" fill="var(--accent-red)"/></svg>
      </li>
      <li>0412-555-083
        <svg viewBox="0 0 16 16"><path d="M4 1l3 3-2 2c1 2 3 4 5 5l2-2 3 3-2 3C7 14 2 9 1 3z" fill="var(--accent-red)"/></svg>
      </li>
      <li>info@meridale.com
        <svg viewBox="0 0 16 16"><rect x="1.5" y="3.5" width="13" height="9" fill="none" stroke="var(--accent-red)" stroke-width="1.5"/><path d="M1.5 3.5l6.5 5 6.5-5" fill="none" stroke="var(--accent-red)" stroke-width="1.5"/></svg>
      </li>
      <li>www.meridale.com
        <svg viewBox="0 0 16 16"><circle cx="8" cy="8" r="6.5" fill="none" stroke="var(--accent-red)" stroke-width="1.5"/><path d="M1.5 8h13M8 1.5c-3 3-3 10 0 13M8 1.5c3 3 3 10 0 13" fill="none" stroke="var(--accent-red)" stroke-width="1.2"/></svg>
      </li>
    </ul>

    <p class="locations">SYDNEY, MELBOURNE,<br>BRISBANE, SINGAPORE</p>
  </section>

</main>
</body>
</html>
```